Web site for Life Coaching Consultant

I require a website for a life coaching business. I have a Velvo Hosting account which I set up last week. I will need to be able to add articles and testimonials. The design should communicate that KT Amber Lantern is there to help people breakdown personal barriers and that we are an advocate to help them achieve personal goals.
Updates

Reason: I have some designers just accepting my invitation to submit so to give them a few days to submit. I have been thrilled with the quality of the submissions Thank you.

Hi everyone

I am loving all your designs.  The only feedback I can get from people is that they feel that the runner makes the web page look like a personal coach rather than a life coach that helps people with relations, career, and personal road blocks.

Sorry                                   

Reason: Hi I have increased the deadline as there has been so many amazing designs and some of you have asked to fine tune your entries. I would like to take this opportunity to thank you all. It is going to be a tough decision. I have put a few more pictures on the project page hoping this will help

Hi I just wanted to thank you all for your great designs.  As I got so many good designs I have asked people to vote.  I will be in touch in the next day or 2.

Cheers

Target Market(s)

People with self esteem issues either woman or girls, people who want to goal set and need an advocate

Industry/Entity Type

Life Coaching

Colors
d2a4cc
e567a6

Requirements
Must have
• must have bio section, logo, articles page, affirmation section and testimonial page.

```html
<!DOCTYPE html>
<html lang="en">
<head>
<meta charset="utf-8">
<title>KT Amber Lantern – Life Coaching</title>
<link href="https://fonts.googleapis.com/css2?family=Arimo:wght@400;700&display=swap" rel="stylesheet">
<style>
  :root{
    --frame:#fe3359;
    --accent:#f0356a;
    --page:#e8e8e8;
    --footer:#d8d8d8;
    --ink:#262626;
    --body:#1f1f1f;
    --muted:#7a7a7a;
    --nav:#5a5a5a;
    --rule:#b9b9b9;
    --rule-dark:#555;
  }
  *{margin:0;padding:0;box-sizing:border-box}
  html,body{width:843px;height:1200px;overflow:hidden}
  body{font-family:"Arimo",Helvetica,Arial,sans-serif;background:var(--frame);position:relative}
  .page{position:absolute;left:8px;top:8px;width:827px;height:1184px;background:var(--page);overflow:hidden}
  .page>*{position:absolute}

  .nav a{position:absolute;top:44px;font-size:12.5px;color:var(--nav);text-decoration:none}
  .nav a.is-active{color:var(--accent)}
  .brand{left:340px;top:12px;width:140px;text-align:center}
  .brand-mark{display:block;margin:0 auto 6px;width:50px;height:50px;border:2.5px solid var(--accent);border-radius:50%}
  .brand-name{font-size:14px;color:var(--accent);white-space:nowrap}

  .rule{height:1px;background:var(--rule)}
  .rule-dark{height:1.5px;background:var(--rule-dark)}

  .visual{display:block}
  .h-sm{font-size:13px;font-weight:400;color:var(--ink);letter-spacing:.2px}
  .h-lg{font-size:23px;font-weight:400;color:var(--ink)}
  .copy{font-size:8.8px;line-height:16px;color:var(--body);text-align:justify}
  .copy-muted{color:var(--muted)}
  .quote-mark{font-size:26px;font-weight:700;color:var(--accent);line-height:1}

  .footer{left:0;top:1084px;width:827px;height:100px;background:var(--footer)}
  .social{position:absolute;top:26px;width:32px;height:32px;border:2px solid #3a3a3a;border-radius:50%}
  .legal{position:absolute;top:70px;width:100%;text-align:center;font-size:9.5px;color:#3a3a3a}
</style>
</head>
<body>
<div class="page">

  <nav class="nav">
    <a class="is-active" href="#" style="left:98px">Home</a>
    <a href="#" style="left:151px">About</a>
    <a href="#" style="left:207px">Article</a>
    <a href="#" style="left:598px">Testimonials</a>
    <a href="#" style="left:690px">Contact</a>
  </nav>
  <div class="brand"><span class="brand-mark"></span><span class="brand-name">KT Amber Lantern</span></div>
  <div class="rule" style="left:100px;top:94px;width:636px"></div>

  <!-- Welcome -->
  <div class="visual" role="img" aria-label="Photo of a woman standing confidently against a sky with the words I am stronger than any excuse" style="left:99px;top:114px;width:418px;height:203px;background:linear-gradient(180deg,#6f87a8 0%,#c9d3df 55%,#e9ecef 80%,#3a302c 100%)"></div>
  <div class="rule-dark" style="left:526px;top:114px;width:200px;height:1px"></div>
  <h2 class="h-sm" style="left:554px;top:140px">WELCOME</h2>
  <div class="rule" style="left:554px;top:168px;width:146px"></div>
  <p class="copy copy-muted" style="left:554px;top:194px;width:146px">Lorem ipsum dolor sit amet, consectetur adipiscing elit. Suspendisse a bibendum arcu. Nullam tincidunt odio sit amet mauris tincidunt sodales. Curabitur non ipsum diam.</p>
  <div class="rule-dark" style="left:526px;top:314px;width:200px;height:1px"></div>

  <!-- Article -->
  <div class="rule-dark" style="left:100px;top:362px;width:398px"></div>
  <h2 class="h-lg" style="left:119px;top:374px">Article</h2>
  <div class="rule" style="left:119px;top:414px;width:317px"></div>
  <p class="copy" style="left:118px;top:440px;width:312px">Lorem ipsum dolor sit amet, consectetur adipiscing elit. Suspendisse a bibendum arcu. Nullam tincidunt odio sit amet mauris tincidunt sodales. Curabitur non ipsum diam. Aliquam vitae est ac enim rutrum molestie.Lorem ipsum dolor sit amet, consectetur adipiscing elit. Suspendisse a bibendum arcu.</p>
  <div class="rule-dark" style="left:100px;top:560px;width:398px"></div>
  <div class="visual" role="img" aria-label="Hand lettered words Dream Big, Set Goals, Take Action" style="left:498px;top:360px;width:258px;height:202px;background:linear-gradient(135deg,#e9e8df,#d4d3c8)"></div>

  <!-- Testimonials -->
  <div class="visual" role="img" aria-label="Handwritten word Testimonials with blue brush strokes" style="left:98px;top:607px;width:260px;height:201px;background:linear-gradient(160deg,#ffffff 60%,#dfe6f0 100%)"></div>
  <div class="rule-dark" style="left:358px;top:609px;width:397px"></div>
  <h2 class="h-lg" style="left:377px;top:620px">Testimonials</h2>
  <div class="rule" style="left:377px;top:662px;width:317px"></div>
  <span class="quote-mark" style="left:386px;top:674px">&ldquo;</span>
  <p class="copy" style="left:375px;top:694px;width:312px;text-indent:26px">Lorem ipsum dolor sit amet, consectetur adipiscing elit. Suspendisse a bibendum arcu. Nullam tincidunt odio sit amet mauris tincidunt sodales. Curabitur non ipsum diam. Aliquam vitae est ac enim rutrum molestie.Lorem ipsum dolor sit amet, consectetur adipiscing elit. Suspendisse a bibendum arcu.</p>
  <span class="quote-mark" style="left:580px;top:768px">&rdquo;</span>
  <div class="rule-dark" style="left:358px;top:807px;width:397px"></div>

  <!-- Affirmation -->
  <div class="visual" role="img" aria-label="Affirmation graphic with the word thankful in a blue speech bubble" style="left:98px;top:850px;width:260px;height:200px;background:linear-gradient(180deg,#1e86d8 0%,#1e86d8 55%,#ffffff 56%,#ffffff 100%)"></div>
  <div class="rule-dark" style="left:358px;top:851px;width:397px"></div>
  <h2 class="h-lg" style="left:377px;top:862px">Affirmation</h2>
  <div class="rule" style="left:377px;top:904px;width:317px"></div>
  <p class="copy" style="left:375px;top:930px;width:312px">Lorem ipsum dolor sit amet, consectetur adipiscing elit. Suspendisse a bibendum arcu. Nullam tincidunt odio sit amet mauris tincidunt sodales. Curabitur non ipsum diam. Aliquam vitae est ac enim rutrum molestie.Lorem ipsum dolor sit amet, consectetur adipiscing elit. Suspendisse a bibendum arcu.</p>
  <div class="rule-dark" style="left:358px;top:1050px;width:397px"></div>

  <footer class="footer">
    <a class="social" href="#" aria-label="Social profile one" style="left:354px"></a>
    <a class="social" href="#" aria-label="Social profile two" style="left:397px"></a>
    <a class="social" href="#" aria-label="Social profile three" style="left:441px"></a>
    <p class="legal">© 2014, All Right &nbsp;Reserved. Power By Norvik Studio</p>
  </footer>

</div>
</body>
</html>
```